Business Card Design Project

- makeup artist business card

- original and creative

- Elegant design

- Feel free to come out with cool designs but stick to being elegant and attractive

- Design relates to makeup

- includes name, occupation, contact numbers, email, website

- regular size business card

- round corner card

- double sided

- on 1 side it should just have the website name in the center " browsandblush.example "

Industry/Entity Type

Business

Requirements
Must have
• Marla Voss
Makeup Artist
USA: +1 (415)872-6410
Singapore: +65 83027715
marlavoss@browsandblush.example
www.browsandblush.example
Should not have
• nothing cartoon looking.
Pictures of makeup being grab from the internet.. Examples: eyes or lips.

```html
<!DOCTYPE html>
<html lang="en">
<head>
<meta charset="utf-8">
<title>Marla Voss – Makeup Artist Business Card</title>
<link rel="stylesheet" href="https://fonts.googleapis.com/css2?family=Great+Vibes&family=Yesteryear&family=Montserrat:wght@700&family=PT+Sans&display=swap">
<style>
  :root {
    --backdrop: #000000;
    --card: #ffffff;
    --gold: #fdb718;
    --violet: #4b0f9e;
    --violet-deep: #3a0a7a;
    --powder: #e98df0;
    --powder-light: #f6c4f7;
    --ink-white: #ffffff;
    --shadow: rgba(60, 40, 60, 0.55);
  }
  * { margin: 0; padding: 0; box-sizing: border-box; }
  html, body {
    width: 1050px;
    height: 1200px;
    overflow: hidden;
    background: var(--backdrop);
  }
  .sheet {
    position: relative;
    width: 1050px;
    height: 1200px;
  }
  .card {
    position: absolute;
    left: 0;
    width: 1050px;
    height: 598px;
    background: var(--card);
    border-radius: 130px;
    overflow: hidden;
  }
  .card--front { top: 0; }
  .card--back { top: 601px; }

  .powder {
    position: absolute;
    left: 0;
    top: 0;
    width: 1050px;
    height: 598px;
  }

  .name {
    position: absolute;
    left: 18px;
    top: 168px;
    font-family: "Great Vibes", cursive;
    font-size: 118px;
    line-height: 1;
    color: var(--gold);
    -webkit-text-stroke: 2px var(--violet);
    paint-order: stroke fill;
    text-shadow: 3px 4px 4px var(--shadow);
    white-space: nowrap;
  }
  .occupation {
    position: absolute;
    left: 70px;
    top: 312px;
    font-family: "Montserrat", sans-serif;
    font-weight: 700;
    font-size: 31px;
    letter-spacing: 0.5px;
    color: var(--violet);
    white-space: nowrap;
  }
  .rule {
    position: absolute;
    left: 468px;
    top: 300px;
    width: 582px;
    height: 4px;
    background: linear-gradient(to bottom, var(--gold) 0 50%, var(--violet-deep) 50% 100%);
  }
  .contact {
    position: absolute;
    font-family: "PT Sans", sans-serif;
    font-size: 29px;
    line-height: 1;
    white-space: nowrap;
    text-shadow: 2px 2px 3px var(--shadow);
  }
  .contact--email { left: 533px; top: 268px; }
  .contact--phones { left: 475px; top: 313px; font-size: 28px; }
  .label { color: var(--ink-white); }
  .value { color: var(--gold); }
  .gap { display: inline-block; width: 12px; }

  .website {
    position: absolute;
    left: 0;
    top: 235px;
    width: 1050px;
    text-align: center;
    font-family: "Yesteryear", cursive;
    font-size: 96px;
    line-height: 1;
    color: var(--gold);
    -webkit-text-stroke: 2px var(--violet);
    paint-order: stroke fill;
    text-shadow: 3px 5px 5px var(--shadow);
    white-space: nowrap;
  }
</style>
</head>
<body>
<main class="sheet">
  <section class="card card--front">
    <svg class="powder" role="img" aria-label="Photograph of loose pink makeup powder" viewBox="0 0 1050 598">
      <defs>
        <radialGradient id="powder-front" cx="0.5" cy="0.5" r="0.5">
          <stop offset="0" stop-color="var(--powder)"/>
          <stop offset="0.75" stop-color="var(--powder)" stop-opacity="0.9"/>
          <stop offset="1" stop-color="var(--powder-light)" stop-opacity="0"/>
        </radialGradient>
      </defs>
      <ellipse cx="540" cy="290" rx="255" ry="265" fill="url(#powder-front)"/>
    </svg>
    <div class="name">Marla Voss</div>
    <div class="occupation">MAKEUP ARTIST</div>
    <div class="rule"></div>
    <p class="contact contact--email"><span class="label">marlavoss@</span><span class="value">browsandblush.example</span></p>
    <p class="contact contact--phones"><span class="label">USA</span> <span class="value">415-872-6410</span><span class="gap"></span><span class="label">Singapore</span> <span class="value">65-83027715</span></p>
  </section>

  <section class="card card--back">
    <svg class="powder" role="img" aria-label="Photograph of loose pink makeup powder" viewBox="0 0 1050 598">
      <defs>
        <radialGradient id="powder-back" cx="0.5" cy="0.5" r="0.5">
          <stop offset="0" stop-color="var(--powder)"/>
          <stop offset="0.75" stop-color="var(--powder)" stop-opacity="0.9"/>
          <stop offset="1" stop-color="var(--powder-light)" stop-opacity="0"/>
        </radialGradient>
      </defs>
      <ellipse cx="530" cy="300" rx="255" ry="265" fill="url(#powder-back)"/>
    </svg>
    <div class="website">www.browsandblush.example</div>
  </section>
</main>
</body>
</html>
```